BRIGHT COLORFUL + 55 FAMILY HISTORY BROCHURE 11 x 17 bifold

11 x 17 Bifold Flyer I have given you the Layout I just need you to make it Pretty

YOU DO NOT NEED TO FOLLOW MY LAYOUT, You can but dont have too

Target Market(s)

55 year old consumers, who could choose our service of Hereditary Cancer Screening

Industry/Entity Type

Health And Wellness

Requirements
Must have
• Must be appealing to Grand Parents, must make them want to test , show lots of pictures of grand children, YOU DO NOT NEED TO FOLLOW MY LAYOUT , You can but dont have too
Nice to have
• use our colors of our logo , YOU DO NOT NEED TO FOLLOW MY LAYOUT , You can but dont have too
Should not have
• YOU DO NOT NEED TO FOLLOW MY LAYOUT, You can but dont have too

```html
<!DOCTYPE html>
<html lang="en">
<head>
<meta charset="utf-8">
<title>Hereditary Cancer Screening Brochure – Outside</title>
<link href="https://fonts.googleapis.com/css2?family=Montserrat:wght@400;500;600;700;800&family=Oswald:wght@600&family=Playfair+Display:ital,wght@1,700&display=swap" rel="stylesheet">
<style>
  :root {
    --navy: #111a45;
    --navy-deep: #0b1236;
    --green: #6cbd3c;
    --green-dark: #3f8d2a;
    --leaf: #8cc63f;
    --ink: #1e2233;
    --paper: #ffffff;
    --stage: #e4e4e6;
    --photo-warm: #d9c2ad;
    --photo-field: #7d8a4a;
  }
  * { margin: 0; padding: 0; box-sizing: border-box; }
  html, body { width: 1200px; height: 878px; overflow: hidden; background: var(--stage); }
  .brochure {
    position: absolute; left: 20px; top: 63px; width: 1160px; height: 751px;
    background: var(--paper); box-shadow: 0 6px 18px rgba(0,0,0,.18);
    font-family: "Montserrat", Arial, sans-serif; color: var(--ink); overflow: hidden;
  }
  .brochure-art { position: absolute; inset: 0; }
  .text { position: absolute; text-align: center; }

  /* Back panel */
  .back-headline { left: 40px; width: 500px; top: 242px; }
  .back-headline .kicker { display: block; font-weight: 800; font-size: 33px; color: var(--green); letter-spacing: .5px; line-height: 38px; }
  .back-headline .question { display: block; font-weight: 500; font-size: 23px; line-height: 28px; }
  .back-headline .promise { display: block; font-weight: 500; font-size: 18.5px; line-height: 28px; }
  .back-lede { left: 40px; width: 500px; top: 344px; font-size: 13.5px; line-height: 18px; }

  .brand { position: absolute; display: flex; align-items: center; gap: 10px; }
  .brand-dot { width: 50px; height: 50px; border-radius: 50%; }
  .brand-name { font-family: "Montserrat", Arial, sans-serif; font-weight: 600; font-size: 18px; line-height: 19px; letter-spacing: 1px; text-transform: uppercase; }
  .brand--back { left: 46px; top: 632px; }
  .brand--back .brand-dot { background: var(--paper); }
  .brand--back .brand-name { color: var(--paper); }
  .brand--front { left: 750px; top: 40px; gap: 14px; }
  .brand--front .brand-dot { width: 88px; height: 88px; background: var(--navy); }
  .brand--front .brand-name { color: var(--navy); font-size: 30px; line-height: 30px; }

  .back-copy { position: absolute; left: 225px; width: 326px; top: 600px; font-size: 11.3px; line-height: 14.8px; color: #e3e6f0; text-align: justify; }
  .back-copy strong { color: var(--green); font-weight: 700; font-size: 12.5px; }
  .web { position: absolute; top: 717px; font-size: 11.5px; letter-spacing: 1.6px; color: var(--green); }
  .web--back { left: 225px; }
  .web--front { left: 770px; }

  /* Front panel */
  .front-title { left: 600px; width: 540px; top: 560px; font-family: "Oswald", "Arial Narrow", sans-serif; font-weight: 600; font-size: 40px; line-height: 48px; color: var(--paper); letter-spacing: -.3px; }
  .front-title .accent { color: var(--green); }
  .front-tagline { left: 600px; width: 540px; top: 605px; font-family: "Playfair Display", Georgia, serif; font-style: italic; font-weight: 700; font-size: 21px; color: var(--green); }
  .front-question { left: 600px; width: 540px; top: 643px; font-size: 19px; line-height: 24px; color: var(--paper); }
  .front-question strong { display: block; color: var(--green); font-weight: 700; }
</style>
</head>
<body>
<main class="brochure">
  <svg class="brochure-art" width="1160" height="751" viewBox="0 0 1160 751" aria-hidden="false">
    <defs>
      <linearGradient id="paperFade" x1="0" y1="0" x2="0" y2="1">
        <stop offset="0" stop-color="#ffffff"/><stop offset="1" stop-color="#f1f3f1"/>
      </linearGradient>
      <linearGradient id="familyFade" x1="0" y1="0" x2="0" y2="1">
        <stop offset="0" stop-color="#dfe6e8" stop-opacity="0"/>
        <stop offset=".35" stop-color="#cfd9df" stop-opacity=".9"/>
        <stop offset="1" stop-color="#c6ccd6"/>
      </linearGradient>
      <linearGradient id="field" x1="0" y1="0" x2="1" y2="1">
        <stop offset="0" stop-color="#5c6a35"/><stop offset=".5" stop-color="#8e9452"/><stop offset="1" stop-color="#6a7a3c"/>
      </linearGradient>
      <linearGradient id="navyFill" x1="0" y1="0" x2="1" y2="0">
        <stop offset="0" stop-color="#0b1236"/><stop offset=".5" stop-color="#16205a"/><stop offset="1" stop-color="#0b1236"/>
      </linearGradient>
      <radialGradient id="warm" cx=".5" cy=".45" r=".6">
        <stop offset="0" stop-color="#e6cfb9"/><stop offset="1" stop-color="#a98d72"/>
      </radialGradient>
      <radialGradient id="leafy" cx=".5" cy=".45" r=".6">
        <stop offset="0" stop-color="#d8c7b3"/><stop offset="1" stop-color="#6f8a4c"/>
      </radialGradient>
    </defs>

    <!-- Back panel -->
    <rect x="0" y="0" width="580" height="751" fill="url(#paperFade)"/>
    <path d="M210,0 C300,40 420,60 580,120 L580,0 Z" fill="var(--leaf)"/>
    <path d="M150,0 C260,60 420,80 580,140 L580,120 C420,60 300,40 210,0 Z" fill="var(--green-dark)" opacity=".35"/>
    <g role="img" aria-label="Photo: grandfather being kissed on the cheek by his granddaughter">
      <path d="M0,0 H230 C250,120 190,220 80,240 C50,244 20,242 0,236 Z" fill="url(#warm)" stroke="var(--green)" stroke-width="7"/>
    </g>
    <g role="img" aria-label="Photo: smiling grandmother hugged by two grandchildren">
      <circle cx="316" cy="100" r="82" fill="url(#warm)" stroke="var(--green)" stroke-width="7"/>
    </g>
    <g role="img" aria-label="Photo: grandparents seated outdoors with their grandchildren">
      <circle cx="481" cy="136" r="74" fill="url(#leafy)" stroke="var(--green)" stroke-width="7"/>
    </g>
    <g role="img" aria-label="Photo: three generations of a family smiling together outdoors">
      <rect x="0" y="370" width="580" height="200" fill="url(#familyFade)"/>
    </g>
    <path d="M0,470 C150,560 330,590 580,485 L580,751 L0,751 Z" fill="var(--green)"/>
    <path d="M0,488 C150,578 330,600 580,500 L580,751 L0,751 Z" fill="var(--paper)"/>
    <path d="M0,500 C150,590 330,610 580,510 L580,751 L0,751 Z" fill="url(#navyFill)"/>

    <!-- Front panel -->
    <g role="img" aria-label="Photo: grandfather's hand holding a small child's hand against a green field">
      <rect x="580" y="0" width="580" height="560" fill="url(#field)"/>
    </g>
    <path d="M580,0 H1160 V62 C1050,150 900,190 760,150 C680,128 620,90 580,60 Z" fill="var(--green-dark)"/>
    <path d="M580,0 H1160 V50 C1050,140 900,176 760,138 C680,116 620,80 580,48 Z" fill="var(--paper)"/>
    <path d="M580,498 C800,440 1000,450 1160,525 L1160,751 L580,751 Z" fill="var(--green)"/>
    <path d="M580,512 C800,458 1000,468 1160,540 L1160,751 L580,751 Z" fill="url(#navyFill)"/>
    <g role="img" aria-label="Photo: young boy and grandfather looking at a plant together">
      <circle cx="682" cy="458" r="74" fill="url(#leafy)" stroke="var(--green)" stroke-width="7"/>
    </g>
    <g role="img" aria-label="Photo: grandmother cheek to cheek with her granddaughter">
      <circle cx="861" cy="443" r="77" fill="url(#warm)" stroke="var(--green)" stroke-width="7"/>
    </g>
    <g role="img" aria-label="Photo: grandparents resting chins on hands with granddaughter behind">
      <circle cx="1062" cy="445" r="82" fill="url(#warm)" stroke="var(--green)" stroke-width="7"/>
    </g>
  </svg>

  <!-- Back panel text -->
  <h2 class="text back-headline">
    <span class="kicker">DOES CANCER</span>
    <span class="question">RUN IN YOUR FAMILY?</span>
    <span class="promise">A Simple Swab Could SAVE a Family Members LIFE</span>
  </h2>
  <p class="text back-lede">Your decision won’t just affect you. It will also impact Your Family, since your test results may Forecast Their Cancer Risks, too.</p>

  <div class="brand brand--back">
    <span class="brand-dot"></span>
    <span class="brand-name">Kinwell<br>Health<br>Group</span>
  </div>
  <p class="back-copy"><strong>We believe it is important to understand what can and cannot be learned with genetic testing.</strong> Genetic mutations can increase risks for certain cancers, but this does not mean cancer will definitely develop. You should be prepared to receive positive or negative results. Most people receive Negative Results meaning no mutations associated with an increased risk for the Hereditary cancers.</p>
  <p class="web web--back">www.kinwellscreening.com</p>

  <!-- Front panel text -->
  <div class="brand brand--front">
    <span class="brand-dot"></span>
    <span class="brand-name">Kinwell<br>Health<br>Group</span>
  </div>
  <h1 class="text front-title">HEREDITARY <span class="accent">CANCER</span> SCREENING</h1>
  <p class="text front-tagline">"The Test You Take For Them"</p>
  <p class="text front-question">Will You give Your loved ones the <strong>Information to Beat Cancer in their lives ?</strong></p>
  <p class="web web--front">www.kinwellscreening.com</p>
</main>
</body>
</html>
```